Stationary

We have designed a new logo and business care.
It is now time for stationary.
We are a financial planning firm and are looking for something more formal that show the strength of our firm.
Please include our tag line; Integrity - Vision -Diligence.
I have uploaded a PDF of our current stationary - but - you are under no obligation to design anything like it.
Thx
Marta
Business

```html
<!DOCTYPE html>
<html lang="en">
<head>
<meta charset="utf-8">
<title>Northwell Trust Partners – Identity Package</title>
<link href="https://fonts.googleapis.com/css2?family=Quicksand:wght@500&family=Open+Sans:wght@400&family=Tinos:ital,wght@0,400;0,700;1,400&display=swap" rel="stylesheet">
<style>
  :root {
    --bg: #e8e9ea;
    --navy: #2b3990;
    --sky: #1a78c2;
    --steel: #7a7d82;
    --paper: #ffffff;
    --ink-grey: #5c5f63;
    --drop: #b1b2b5;
    --faint: #e4e6f2;
  }
  * { margin: 0; padding: 0; box-sizing: border-box; }
  html, body { width: 1200px; height: 900px; overflow: hidden; background: var(--bg); }
  .canvas { position: relative; width: 1200px; height: 900px; }
  address { font-style: normal; }

  .brand { position: absolute; display: flex; flex-direction: column; align-items: center; }
  .brand-row { display: flex; align-items: center; gap: 8px; }
  .brand-dot { border-radius: 50%; background: var(--navy); }
  .brand-name { font-family: "Quicksand", sans-serif; font-weight: 500; color: var(--navy); white-space: nowrap; line-height: 1.1; }
  .brand-tag { font-family: "Quicksand", sans-serif; font-weight: 500; color: var(--steel); white-space: nowrap; line-height: 1.1; }
  .brand.on-dark .brand-dot { background: #fff; }
  .brand.on-dark .brand-name, .brand.on-dark .brand-tag { color: #fff; }

  .title-brand { left: 328px; top: 90px; }
  .title-brand .brand-dot { width: 18px; height: 18px; }
  .title-brand .brand-name { font-size: 22px; }
  .title-brand .brand-tag { font-size: 11px; letter-spacing: 4px; margin-top: 8px; }

  .package-title { position: absolute; left: 613px; top: 102px; font-family: "Open Sans", sans-serif; font-weight: 400; font-size: 29px; color: var(--sky); letter-spacing: 0.3px; line-height: 1.2; }

  .sheet { position: absolute; background: var(--paper); box-shadow: 0 5px 0 var(--drop); overflow: hidden; }

  .contact { font-family: "Tinos", serif; font-weight: 700; color: var(--ink-grey); line-height: 1.55; }

  .letterhead { left: 124px; top: 193px; width: 465px; height: 602px; }
  .letterhead .contact { position: absolute; left: 34px; top: 50px; font-size: 9px; }
  .letterhead .brand { right: 32px; top: 84px; }
  .letterhead .brand-dot { width: 11px; height: 11px; }
  .letterhead .brand-name { font-size: 14px; }
  .letterhead .brand-tag { font-size: 7.5px; letter-spacing: 2.8px; margin-top: 5px; }
  .letterhead .rule { position: absolute; left: 14px; top: 126px; width: 438px; height: 1px; background: var(--navy); }
  .letterhead .backdrop-name { position: absolute; left: 0; right: 0; top: 255px; text-align: center; font-family: "Quicksand", sans-serif; font-weight: 500; font-size: 110px; color: var(--faint); line-height: 1.2; }
  .letterhead .footer-band { position: absolute; left: 0; bottom: 0; width: 465px; height: 38px; }

  .card-front { left: 603px; top: 265px; width: 191px; height: 110px; background: var(--navy); }
  .card-front .brand { left: 0; right: 0; top: 50px; }
  .card-front .brand-dot { width: 9px; height: 9px; }
  .card-front .brand-name { font-size: 12px; }
  .card-front .brand-tag { font-size: 6px; letter-spacing: 2.2px; margin-top: 4px; }

  .card-back { left: 821px; top: 265px; width: 191px; height: 110px; }
  .card-back .brand { right: 14px; top: 42px; }
  .card-back .brand-dot { width: 6px; height: 6px; }
  .card-back .brand-name { font-size: 8.5px; }
  .card-back .brand-tag { font-size: 4.5px; letter-spacing: 1.5px; margin-top: 2px; }
  .card-back .card-address { position: absolute; right: 16px; top: 60px; text-align: right; font-family: "Tinos", serif; font-style: italic; font-size: 5.5px; color: var(--navy); line-height: 1.25; }
  .card-back .holder { position: absolute; left: 15px; top: 66px; font-family: "Tinos", serif; color: var(--navy); line-height: 1.3; }
  .holder .holder-name { font-size: 9px; }
  .holder .holder-role { font-size: 5.5px; }
  .holder .holder-line { font-size: 5.5px; font-weight: 700; }

  .envelope { left: 604px; top: 391px; width: 519px; height: 226px; }
  .envelope .brand { left: 22px; top: 76px; align-items: flex-start; }
  .envelope .brand-dot { width: 12px; height: 12px; }
  .envelope .brand-name { font-size: 16px; }
  .envelope .brand-tag { font-size: 8px; letter-spacing: 3px; margin-top: 4px; }
  .envelope .contact { position: absolute; left: 22px; top: 113px; font-size: 9px; }
</style>
</head>
<body>
<main class="canvas">

  <div class="brand title-brand">
    <div class="brand-row"><span class="brand-dot"></span><span class="brand-name">Northwell Trust Partners</span></div>
    <span class="brand-tag">Clarity Strength Care</span>
  </div>
  <h1 class="package-title">IDENTITY PACKAGE</h1>

  <section class="sheet letterhead">
    <address class="contact">
      2270 W Aldercrest Ave, Millbrook, OR 97390<br>
      Tel &nbsp;: (541) 555-0142<br>
      Fax :(541) 555-0143
    </address>
    <div class="brand">
      <div class="brand-row"><span class="brand-dot"></span><span class="brand-name">Northwell Trust Partners</span></div>
      <span class="brand-tag">Clarity Strength Care</span>
    </div>
    <div class="rule"></div>
    <div class="backdrop-name" aria-hidden="true">NTP</div>
    <svg class="footer-band" viewBox="0 0 465 38" aria-hidden="true">
      <rect x="0" y="0" width="465" height="38" fill="var(--sky)"/>
      <polygon points="0,0 205,0 243,38 0,38" fill="var(--navy)"/>
      <polygon points="193,0 215,0 253,38 231,38" fill="var(--steel)"/>
    </svg>
  </section>

  <section class="sheet card-front">
    <div class="brand on-dark">
      <div class="brand-row"><span class="brand-dot"></span><span class="brand-name">Northwell Trust Partners</span></div>
      <span class="brand-tag">Clarity Strength Care</span>
    </div>
  </section>

  <section class="sheet card-back">
    <div class="brand">
      <div class="brand-row"><span class="brand-dot"></span><span class="brand-name">Northwell Trust Partners</span></div>
      <span class="brand-tag">Clarity Strength Care</span>
    </div>
    <address class="card-address">
      2270 W Aldercrest Ave, Millbrook, OR 97390<br>
      Tel : (541) 555-0142<br>
      Fax : (541) 555-0143
    </address>
    <div class="holder">
      <div class="holder-name">Marta</div>
      <div class="holder-role">Advisor</div>
      <div class="holder-line">Tel : (541) 555-0144</div>
      <div class="holder-line">Email : marta@northwelltrust.com</div>
    </div>
  </section>

  <section class="sheet envelope">
    <div class="brand">
      <div class="brand-row"><span class="brand-dot"></span><span class="brand-name">Northwell Trust Partners</span></div>
      <span class="brand-tag">Clarity Strength Care</span>
    </div>
    <address class="contact">
      2270 W Aldercrest Ave, Millbrook, OR 97390<br>
      Tel &nbsp;: (541) 555-0142<br>
      Fax :(541) 555-0143
    </address>
  </section>

</main>
</body>
</html>
```